Tandle Repair - Handyman and Home Repair Services

I need a business card/letterhead logo for my new handyman service in my local area. I'm happy for a logo design to be done prior to business card design so it can be incorporated on to the card, for which I'd be happy to pay more for. I'd like it to be modern and not using the typical pictures of tools and cartoon characters in dungarees! I like the idea of tools but in a more modern way i.e subtle background images in different shades to main colour. I do like the american retro designs and those that show age and patina for example, having an image half old, half new in its appearance to represent the repairing of things. Colours in mind are 1950's retro colours, ie using grey with pastel greens, red and cream. I'd like to break the mould and the stigma thats attached to these jobs and make it more cool and up to date. I hope this will attract interior designers and more modern businesses to use my services.

This is the logo design I like and would be happy for this idea and colours:

http://toast-a-roam.co.uk/wp-content/uploads/2011/01/t-r_logo600px.png

```html
<!DOCTYPE html>
<html lang="en">
<head>
<meta charset="utf-8">
<title>Tandle Repair – Business Card</title>
<link rel="stylesheet" href="https://fonts.googleapis.com/css2?family=Lato:wght@400;700&family=Dancing+Script:wght@400&display=swap">
<style>
  :root {
    --page: #f4f4f4;
    --card: #262626;
    --card-deep: #1e1e1e;
    --pattern: #303030;
    --green: #8cc63f;
    --cream: #f3e2a6;
    --text-font: "Lato", "Gill Sans", sans-serif;
    --script-font: "Dancing Script", cursive;
  }
  * { box-sizing: border-box; margin: 0; padding: 0; }
  html, body {
    width: 1200px;
    height: 900px;
    overflow: hidden;
    background: var(--page);
  }
  .canvas {
    position: relative;
    width: 1200px;
    height: 900px;
  }
  .card {
    position: absolute;
    top: 280px;
    width: 540px;
    height: 340px;
    border-radius: 30px;
    background: var(--card-deep);
    padding: 8px;
    box-shadow: 0 14px 30px rgba(0,0,0,0.18);
  }
  .card--front { left: 40px; }
  .card--back { left: 620px; }
  .card__frame {
    position: relative;
    width: 100%;
    height: 100%;
    border: 6px solid var(--green);
    border-radius: 24px;
    overflow: hidden;
  }
  .card__texture {
    position: absolute;
    inset: 0;
    background: radial-gradient(ellipse at center, var(--pattern) 0%, var(--card) 75%);
  }
  .card__content {
    position: relative;
    height: 100%;
    display: flex;
    flex-direction: column;
    align-items: center;
    justify-content: center;
    text-align: center;
    color: var(--cream);
    font-family: var(--text-font);
  }
  .brand {
    display: flex;
    align-items: center;
    gap: 14px;
  }
  .brand__dot {
    width: 40px;
    height: 40px;
    border-radius: 50%;
    background: var(--green);
  }
  .brand__name {
    font-family: var(--text-font);
    font-weight: 700;
    color: var(--cream);
  }
  .card--front .brand__name { font-size: 46px; }
  .card--back .brand { margin-top: -18px; }
  .card--back .brand__dot { width: 26px; height: 26px; }
  .card--back .brand__name { font-size: 30px; }
  .tagline {
    margin-top: 16px;
    font-family: var(--script-font);
    font-size: 21px;
    color: var(--cream);
  }
  .contact__name {
    margin-top: 26px;
    font-size: 24px;
    font-weight: 700;
    color: var(--green);
  }
  .contact__phone {
    margin-top: 20px;
    font-size: 19px;
  }
  .contact__web {
    margin-top: 4px;
    font-size: 19px;
  }
</style>
</head>
<body>
<main class="canvas">
  <section class="card card--front">
    <div class="card__frame">
      <div class="card__texture" role="img" aria-label="Faint pattern of handyman tools in slightly lighter grey"></div>
      <div class="card__content">
        <div class="brand">
          <span class="brand__dot"></span>
          <span class="brand__name">Tandle Repair</span>
        </div>
      </div>
    </div>
  </section>

  <section class="card card--back">
    <div class="card__frame">
      <div class="card__texture" role="img" aria-label="Faint pattern of handyman tools in slightly lighter grey"></div>
      <div class="card__content">
        <div class="brand">
          <span class="brand__dot"></span>
          <span class="brand__name">Tandle Repair</span>
        </div>
        <p class="tagline">Handyman services from repair to install</p>
        <p class="contact__name">Owen Hartley</p>
        <p class="contact__phone">07700 900412</p>
        <p class="contact__web">www.tandlerepair.co.uk</p>
      </div>
    </div>
  </section>
</main>
</body>
</html>
```